PROPERTY MANAGEMENT AND REAL ESTATE

Target Market(s)

real estate owners and investors

Industry/Entity Type

Real Estate

Contact Information for Business Card

BRIGHT LANTERN PROPERTY MANAGEMENT GROUP, LLC
487 North Corwin Parkway
Suite 260
Marlow Shores, FL 33127

```html
<!DOCTYPE html>
<html lang="en">
<head>
<meta charset="utf-8">
<title>Bright Lantern Property Management Group — Business Cards</title>
<link rel="stylesheet" href="https://fonts.googleapis.com/css2?family=Open+Sans:wght@300;400&family=Orbitron:wght@800&display=swap">
<style>
  :root {
    --canvas: #e9e8e6;
    --card: #ffffff;
    --brand-red: #a8191f;
    --ink: #1b1b1b;
    --muted: #7d7d7d;
    --tint: #f4e6e3;
    --card-shadow: 0 6px 18px rgba(0, 0, 0, 0.18);
  }
  * { box-sizing: border-box; margin: 0; padding: 0; }
  html, body {
    width: 1200px;
    height: 872px;
    overflow: hidden;
    background: var(--canvas);
  }
  .canvas {
    position: relative;
    width: 1200px;
    height: 872px;
  }
  .card {
    position: absolute;
    top: 281px;
    width: 540px;
    height: 309px;
    background: var(--card);
    box-shadow: var(--card-shadow);
    overflow: hidden;
  }
  .card--front { left: 40px; }
  .card--back { left: 620px; }

  /* Front: contact side */
  .front__watermark {
    position: absolute;
    left: 270px;
    top: 80px;
    width: 220px;
    height: 220px;
    border-radius: 50%;
    background: var(--tint);
  }
  .front__brand {
    position: absolute;
    left: 26px;
    top: 22px;
    display: flex;
    align-items: center;
    gap: 14px;
  }
  .brand-dot {
    width: 58px;
    height: 58px;
    border-radius: 50%;
    background: var(--brand-red);
    flex: none;
  }
  .front__name {
    font-family: "Open Sans", sans-serif;
    font-weight: 300;
    font-size: 13px;
    line-height: 1.25;
    letter-spacing: 0.02em;
    color: var(--muted);
    text-transform: uppercase;
  }
  .front__contact {
    position: absolute;
    left: 26px;
    top: 104px;
    font-family: "Open Sans", sans-serif;
    font-weight: 400;
    font-size: 17px;
    line-height: 1.3;
    color: var(--ink);
    font-style: normal;
  }
  .front__phones { margin-top: 22px; }

  /* Back: brand side */
  .back__swoosh {
    position: absolute;
    inset: 0;
    width: 540px;
    height: 309px;
  }
  .back__name {
    position: absolute;
    right: 18px;
    top: 26px;
    width: 400px;
    font-family: "Orbitron", sans-serif;
    font-weight: 800;
    font-size: 16px;
    line-height: 1.35;
    letter-spacing: 0.05em;
    color: var(--ink);
    text-align: center;
    text-transform: uppercase;
  }
  .back__mark {
    position: absolute;
    left: 372px;
    top: 104px;
    width: 76px;
    height: 76px;
    border-radius: 50%;
    background: var(--brand-red);
  }
</style>
</head>
<body>
<main class="canvas">

  <section class="card card--front" aria-label="Business card, contact side">
    <div class="front__watermark" aria-hidden="true"></div>
    <div class="front__brand">
      <span class="brand-dot" aria-hidden="true"></span>
      <p class="front__name">Bright Lantern Property<br>Management Group, LLC</p>
    </div>
    <address class="front__contact">
      <p>487 North Corwin Parkway, Suite 260</p>
      <p>Marlow Shores,</p>
      <p>FL 33127</p>
      <div class="front__phones">
        <p>Tel.&nbsp; 305-555-0142</p>
        <p>Fax.&nbsp; 786-555-0187</p>
      </div>
    </address>
  </section>

  <section class="card card--back" aria-label="Business card, brand side">
    <svg class="back__swoosh" viewBox="0 0 540 309" aria-hidden="true">
      <path d="M0 0 H34 C110 70 230 170 300 225 C340 256 372 284 392 309 H0 Z" fill="var(--brand-red)"/>
    </svg>
    <h1 class="back__name">Bright Lantern Property<br>Management Group, LLC</h1>
    <span class="back__mark" aria-hidden="true"></span>
  </section>

</main>
</body>
</html>
```